REDESIGN MAIN BANNER IMAGE FOR MARKETING WEBSITE

I feel like my main banner image is too busy but I like it but i want to see other options. www.brightlanepromoworks.biz I want a nice professional clean design that goes with current theme of site. Must look professional and show the variety of incentives we offer but not be overwelming.

My business is called Brightlane Promo Works and I provide businesses around the world with marketing incentives that they can use to create exciting promotions and contest and marketing giveaways to help attract more customers.

I provide a variety of different types of incentives such as Vacation Certificates, Dining Vouchers, Hotel Savings Cards, Smart Watches, Etc. that businesses can use in their marketing efforts.

I want my main banner image to reflect the variety of different categories of incentives... that I offer here: https://www.brightlanepromoworks.biz/incentives

We can use images of certificates or images.....I just want the content to be the same:

CONTENT FOR MAIN BANNER IMAGE:
INCREASE LEADS AND SALES OVERNIGHT

CREATE EXCITING MARKETING PROMOTIONS GIVING AWAY SMART DEVICES, VACATION CERTIFICATES, DINING VOUCHERS AND OTHER INCENTIVES TO YOUR CUSTOMERS

GET A FREE SAMPLE PACKAGE FOR A LIMITED TIME ONLY

Target Market(s)

b2b business owners, ceo, president, owner, founder

Industry/Entity Type

Promotional

Requirements
Must have
• Hi guys keep in mind the finished product will have to be 1800x840

Nice to have
• I want a nice professional clean design that goes with current theme of site. Must look professional and show the variety of incentives we offer but not be overwelming.
Should not have

```html
<!DOCTYPE html>
<html lang="en">
<head>
<meta charset="utf-8">
<title>Brightlane Promo Works – Increase Leads and Sales Overnight</title>
<link href="https://fonts.googleapis.com/css2?family=Roboto:wght@300;400;900&family=Roboto+Condensed:wght@300;400;700&family=Oswald:wght@400;600&display=swap" rel="stylesheet">
<style>
  :root {
    --ink-dark: #1b1d22;
    --ink-mid: #3a3d44;
    --headline-white: #ffffff;
    --leads-blue: #1f7fd6;
    --overnight-green: #3ccf3c;
    --cta-blue: #2d86c9;
    --cta-green: #3ec63b;
    --cert-red: #c3161c;
    --cert-yellow: #ffe23a;
    --paper: #ffffff;
    --text-grey: #55585e;
    --rule-grey: #c9cbcf;
  }
  * { box-sizing: border-box; margin: 0; padding: 0; }
  html, body { width: 1200px; height: 560px; overflow: hidden; background: var(--paper); }
  .banner { position: relative; width: 1200px; height: 560px; overflow: hidden; background: var(--paper); font-family: 'Roboto', sans-serif; }

  .banner__backdrop {
    position: absolute; left: 0; top: 0; width: 1200px; height: 343px;
    background: radial-gradient(ellipse at 50% 30%, #4a4d53 0%, #2b2d32 45%, #15171b 100%);
  }
  .banner__rule { position: absolute; left: 0; top: 341px; width: 1200px; height: 5px; background: var(--overnight-green); }

  .headline {
    position: absolute; left: 0; top: 44px; width: 1200px; text-align: center;
    font-size: 47px; line-height: 1; color: var(--headline-white); font-weight: 400; letter-spacing: 0.5px;
  }
  .headline__strong { font-weight: 900; color: var(--leads-blue); }
  .headline__green { font-weight: 400; color: var(--overnight-green); }

  .subline {
    position: absolute; left: 0; top: 117px; width: 1200px; text-align: center;
    font-family: 'Roboto Condensed', sans-serif; font-weight: 300; font-size: 16.5px;
    color: var(--headline-white); letter-spacing: -0.2px;
  }

  .certs { position: absolute; left: 75px; top: 172px; display: flex; }
  .cert {
    position: relative; width: 132px; height: 208px; background: var(--paper); overflow: hidden;
    box-shadow: 0 2px 6px rgba(0,0,0,0.45); border-right: 1px solid #ddd;
  }
  .cert__photo { position: absolute; left: 0; top: 0; width: 132px; height: 96px; }
  .cert__compliments { position: absolute; right: 4px; top: 4px; font-size: 3.5px; color: #888; font-family: 'Roboto Condensed', sans-serif; }
  .cert__enjoy {
    position: absolute; left: 6px; top: 3px; font-family: 'Oswald', sans-serif; font-weight: 600;
    font-size: 20px; line-height: 1; color: var(--paper); text-shadow: 0 1px 2px rgba(0,0,0,0.6);
  }
  .cert__eyebrow { position: absolute; left: 46px; top: 5px; font-family: 'Roboto Condensed', sans-serif; font-size: 5px; color: var(--paper); text-transform: uppercase; }
  .cert__tag {
    position: absolute; left: 46px; top: 12px; background: var(--cert-red); color: var(--cert-yellow);
    font-family: 'Oswald', sans-serif; font-weight: 600; font-size: 7.5px; padding: 1px 3px; line-height: 1.1; text-transform: uppercase;
  }
  .cert__offer {
    position: absolute; left: 6px; top: 27px; width: 100px; font-size: 5.2px; line-height: 1.25;
    color: var(--paper); font-weight: 400; text-shadow: 0 0 2px rgba(0,0,0,0.7);
  }
  .cert__offer em { font-style: normal; color: var(--cert-yellow); }
  .cert__badge {
    position: absolute; right: -12px; top: 70px; width: 36px; height: 36px; border-radius: 50%;
    border: 3px solid var(--cert-red);
  }
  .cert__ribbon {
    position: absolute; left: 0; top: 96px; width: 110px; height: 8px; background: var(--cert-red);
    color: var(--paper); font-size: 3.6px; line-height: 8px; padding-left: 6px; font-weight: 700;
  }
  .cert__body { position: absolute; left: 6px; top: 108px; width: 118px; font-size: 3.4px; line-height: 1.3; color: var(--text-grey); }
  .cert__heading {
    position: absolute; left: 6px; width: 34px; height: 5px; background: var(--cert-red); color: var(--paper);
    font-size: 3.2px; line-height: 5px; padding-left: 2px; font-weight: 700;
  }
  .cert__heading--features { top: 122px; }
  .cert__heading--how { top: 150px; width: 44px; }
  .cert__lines { position: absolute; left: 6px; top: 129px; width: 118px; }
  .cert__line { height: 1.4px; background: var(--rule-grey); margin-bottom: 2.6px; }
  .cert__line--half { width: 55%; }
  .cert__lines--how { top: 157px; }
  .cert__footer { position: absolute; left: 0; top: 180px; width: 132px; height: 28px; border-top: 1px solid #e3e3e3; }
  .cert__id { position: absolute; left: 6px; top: 5px; width: 34px; text-align: center; font-size: 3.4px; color: var(--ink-dark); line-height: 1.35; }
  .cert__id b { color: var(--cert-red); font-size: 4.2px; }
  .cert__site { position: absolute; left: 44px; top: 5px; width: 86px; text-align: center; font-size: 3.3px; color: var(--ink-dark); line-height: 1.35; font-weight: 700; }
  .cert__site b { color: var(--cert-red); font-size: 4.6px; font-weight: 900; }
  .cert__terms { display: block; font-weight: 400; font-size: 2.8px; }

  .cta { position: absolute; left: 105px; top: 424px; width: 1014px; height: 79px; }
  .cta__shape { position: absolute; left: 0; top: 0; }
  .cta__main {
    position: absolute; left: 0; top: 0; width: 840px; height: 79px; line-height: 79px; text-align: center;
    color: var(--headline-white); font-size: 31px; font-weight: 300; letter-spacing: -0.3px;
  }
  .cta__main strong { font-weight: 900; }
  .cta__offer {
    position: absolute; left: 855px; top: 9px; width: 170px; text-align: center; color: var(--headline-white);
    font-family: 'Roboto Condensed', sans-serif; font-size: 19px; line-height: 22px; font-weight: 300;
  }
  .cta__offer strong { font-weight: 700; font-size: 21px; }
</style>
</head>
<body>
<main class="banner">
  <div class="banner__backdrop" role="img" aria-label="Businessman in a dark suit touching a glowing digital screen"></div>
  <div class="banner__rule"></div>

  <h1 class="headline">INCREASE <span class="headline__strong">LEADS</span> AND <span class="headline__strong">SALES</span> <span class="headline__green">OVERNIGHT</span></h1>
  <p class="subline">CREATE EXCITING MARKETING PROMOTIONS GIVING AWAY SMART DEVICES, VACATION CERTIFICATES, DINING VOUCHERS AND OTHER INCENTIVES TO YOUR CUSTOMERS</p>

  <section class="certs" aria-label="Incentive certificates">
    <article class="cert">
      <div class="cert__photo" role="img" aria-label="Mexico beach resort with pool and palm trees" style="background:linear-gradient(180deg,#5b8fc4 0%,#8fb6d6 40%,#3f8f8a 75%,#c9b48a 100%)"></div>
      <span class="cert__compliments">Compliments Of</span>
      <span class="cert__enjoy">ENJOY</span><span class="cert__eyebrow">Mexico Resort</span><span class="cert__tag">Luxury</span>
      <p class="cert__offer">4 Night Mexico Beach <em>Resort Getaway</em></p>
      <div class="cert__badge" role="img" aria-label="Resort detail photo" style="background:linear-gradient(#4aa0c8,#2f7f6a)"></div>
      <div class="cert__ribbon">EXCLUSIVELY FOR : CUSTOMER NAME</div>
      <p class="cert__body">Congratulations, you have been awarded this reward.</p>
      <div class="cert__heading cert__heading--features">FEATURES</div>
      <div class="cert__lines"><div class="cert__line"></div><div class="cert__line"></div><div class="cert__line cert__line--half"></div></div>
      <div class="cert__heading cert__heading--how">HOW CAN WE DO THIS?</div>
      <div class="cert__lines cert__lines--how"><div class="cert__line"></div><div class="cert__line"></div><div class="cert__line cert__line--half"></div></div>
      <div class="cert__footer"><p class="cert__id">Certificate ID<br><b>#10983-95930</b><br>Expires 02/29/2020</p><p class="cert__site">VIEW ALL THE DETAILS OF THIS SPECIAL<br><b>WWW.PRIZEPATHREWARDS.COM</b><span class="cert__terms">Terms and conditions apply</span></p></div>
    </article>

    <article class="cert">
      <div class="cert__photo" role="img" aria-label="Luxury resort lagoon and overwater villas" style="background:linear-gradient(180deg,#3d7fc0 0%,#7ab8dd 45%,#2aa6a8 80%,#d9c9a0 100%)"></div>
      <span class="cert__compliments">Compliments Of</span>
      <span class="cert__enjoy">ENJOY</span><span class="cert__eyebrow">Couple Only</span><span class="cert__tag">In A Luxury Resort</span>
      <p class="cert__offer">7 Nights Luxury Resort Getaway <em>Over 3000 Locations Worldwide To Choose From</em></p>
      <div class="cert__badge" role="img" aria-label="Resort beach photo" style="background:linear-gradient(#6fb3d9,#c9b27a)"></div>
      <div class="cert__ribbon">EXCLUSIVELY FOR : CUSTOMER NAME</div>
      <p class="cert__body">Congratulations, you have been awarded this reward.</p>
      <div class="cert__heading cert__heading--features">FEATURES</div>
      <div class="cert__lines"><div class="cert__line"></div><div class="cert__line"></div><div class="cert__line cert__line--half"></div></div>
      <div class="cert__heading cert__heading--how">HOW CAN WE DO THIS?</div>
      <div class="cert__lines cert__lines--how"><div class="cert__line"></div><div class="cert__line"></div><div class="cert__line cert__line--half"></div></div>
      <div class="cert__footer"><p class="cert__id">Certificate ID<br><b>#10983-95930</b><br>Expires 02/29/2020</p><p class="cert__site">VIEW ALL THE DETAILS OF THIS SPECIAL<br><b>WWW.PRIZEPATHREWARDS.COM</b><span class="cert__terms">Terms and conditions apply</span></p></div>
    </article>

    <article class="cert">
      <div class="cert__photo" role="img" aria-label="Group of friends dining at a restaurant" style="background:linear-gradient(180deg,#2a1e18 0%,#5a3a26 45%,#8a5a34 75%,#c89a62 100%)"></div>
      <span class="cert__compliments">Compliments Of</span>
      <span class="cert__enjoy">ENJOY</span><span class="cert__tag" style="top:8px;font-size:9px">$25 OFF</span>
      <p class="cert__offer">$25 Off At Thousands Of <em>Participating Restaurants</em></p>
      <div class="cert__badge" role="img" aria-label="Plated meal photo" style="background:linear-gradient(#9a6a3a,#3a2a1a)"></div>
      <div class="cert__ribbon">EXCLUSIVELY FOR : CUSTOMER NAME</div>
      <p class="cert__body">Congratulations, you have been awarded this reward.</p>
      <div class="cert__heading cert__heading--features">FEATURES</div>
      <div class="cert__lines"><div class="cert__line"></div><div class="cert__line"></div><div class="cert__line cert__line--half"></div></div>
      <div class="cert__heading cert__heading--how">HOW CAN WE DO THIS?</div>
      <div class="cert__lines cert__lines--how"><div class="cert__line"></div><div class="cert__line"></div><div class="cert__line cert__line--half"></div></div>
      <div class="cert__footer"><p class="cert__id">Certificate ID<br><b>#10983-95930</b><br>Expires 02/29/2020</p><p class="cert__site">VIEW ALL THE DETAILS OF THIS SPECIAL<br><b>WWW.PRIZEPATHREWARDS.COM</b><span class="cert__terms">Terms and conditions apply</span></p></div>
    </article>

    <article class="cert">
      <div class="cert__photo" role="img" aria-label="Hotel lobby lounge interior" style="background:linear-gradient(180deg,#3a2f28 0%,#6a5440 45%,#8c7a62 75%,#4a3a2c 100%)"></div>
      <span class="cert__compliments">Compliments Of</span>
      <span class="cert__enjoy">ENJOY</span><span class="cert__eyebrow">A 2 Night</span><span class="cert__tag">Hotel Stay</span>
      <p class="cert__offer">of 3+ Star Hotel Accommodations <em>In The City Of Your Choice Of Over 50 Of The Most Popular Destinations Available!</em></p>
      <div class="cert__badge" role="img" aria-label="Hotel room photo" style="background:linear-gradient(#b49a74,#5a4632)"></div>
      <div class="cert__ribbon">EXCLUSIVELY FOR : CUSTOMER NAME</div>
      <p class="cert__body">Congratulations, you have been awarded this reward.</p>
      <div class="cert__heading cert__heading--features">FEATURES</div>
      <div class="cert__lines"><div class="cert__line"></div><div class="cert__line"></div><div class="cert__line cert__line--half"></div></div>
      <div class="cert__heading cert__heading--how">HOW CAN WE DO THIS?</div>
      <div class="cert__lines cert__lines--how"><div class="cert__line"></div><div class="cert__line"></div><div class="cert__line cert__line--half"></div></div>
      <div class="cert__footer"><p class="cert__id">Certificate ID<br><b>#10983-95930</b><br>Expires 02/29/2020</p><p class="cert__site">VIEW ALL THE DETAILS OF THIS SPECIAL<br><b>WWW.PRIZEPATHREWARDS.COM</b><span class="cert__terms">Terms and conditions apply</span></p></div>
    </article>

    <article class="cert">
      <div class="cert__photo" role="img" aria-label="Traveller with luggage in a hotel corridor" style="background:linear-gradient(180deg,#2c3a4c 0%,#4a5a6e 45%,#7a6a52 80%,#3a3026 100%)"></div>
      <span class="cert__compliments">Compliments Of</span>
      <span class="cert__enjoy">ENJOY</span><span class="cert__tag" style="top:8px;font-size:9px">$200 OFF</span>
      <p class="cert__offer">Get $200 Off At Over 400,000 <em>Hotel &amp; Resort Properties Worldwide!</em></p>
      <div class="cert__badge" role="img" aria-label="Resort pool photo" style="background:linear-gradient(#5aa0c8,#2c5a7a)"></div>
      <div class="cert__ribbon">EXCLUSIVELY FOR : CUSTOMER NAME</div>
      <p class="cert__body">Congratulations, you have been awarded this reward.</p>
      <div class="cert__heading cert__heading--features">FEATURES</div>
      <div class="cert__lines"><div class="cert__line"></div><div class="cert__line"></div><div class="cert__line cert__line--half"></div></div>
      <div class="cert__heading cert__heading--how">HOW CAN WE DO THIS?</div>
      <div class="cert__lines cert__lines--how"><div class="cert__line"></div><div class="cert__line"></div><div class="cert__line cert__line--half"></div></div>
      <div class="cert__footer"><p class="cert__id">Certificate ID<br><b>#10983-95930</b><br>Expires 02/29/2020</p><p class="cert__site">VIEW ALL THE DETAILS OF THIS SPECIAL<br><b>WWW.PRIZEPATHREWARDS.COM</b><span class="cert__terms">Terms and conditions apply</span></p></div>
    </article>

    <article class="cert">
      <div class="cert__photo" role="img" aria-label="Row of colourful touch screen media players" style="background:linear-gradient(180deg,#e9e9ee 0%,#b8b8d8 40%,#6a5ad0 70%,#3a3a4a 100%)"></div>
      <span class="cert__compliments">Compliments Of</span>
      <span class="cert__enjoy">ENJOY</span><span class="cert__eyebrow">Your Brand New</span><span class="cert__tag">MP4 Player</span>
      <p class="cert__offer">Enjoy Your Brand New <em>Touch Screen MP4 Player</em></p>
      <div class="cert__badge" role="img" aria-label="Media player close-up photo" style="background:linear-gradient(#8a7ae0,#2a2a3a)"></div>
      <div class="cert__ribbon">EXCLUSIVELY FOR : CUSTOMER NAME</div>
      <p class="cert__body">Congratulations, you have been awarded this reward.</p>
      <div class="cert__heading cert__heading--features">FEATURES</div>
      <div class="cert__lines"><div class="cert__line"></div><div class="cert__line"></div><div class="cert__line cert__line--half"></div></div>
      <div class="cert__heading cert__heading--how">HOW CAN WE DO THIS?</div>
      <div class="cert__lines cert__lines--how"><div class="cert__line"></div><div class="cert__line"></div><div class="cert__line cert__line--half"></div></div>
      <div class="cert__footer"><p class="cert__id">Certificate ID<br><b>#10983-95930</b><br>Expires 02/29/2020</p><p class="cert__site">VIEW ALL THE DETAILS OF THIS SPECIAL<br><b>WWW.PRIZEPATHREWARDS.COM</b><span class="cert__terms">Terms and conditions apply</span></p></div>
    </article>

    <article class="cert">
      <div class="cert__photo" role="img" aria-label="Wireless earbuds with charging case and tablet user" style="background:linear-gradient(180deg,#f2f2f2 0%,#d8d8d8 45%,#b89a7a 75%,#6a5040 100%)"></div>
      <span class="cert__compliments">Compliments Of</span>
      <span class="cert__enjoy">ENJOY</span><span class="cert__eyebrow">Your Brand New</span><span class="cert__tag">Earbuds</span>
      <p class="cert__offer">Premium Wireless Earbuds <em>Powered by Smart OS</em></p>
      <div class="cert__badge" role="img" aria-label="Earbuds close-up photo" style="background:linear-gradient(#fafafa,#bcbcbc)"></div>
      <div class="cert__ribbon">EXCLUSIVELY FOR : CUSTOMER NAME</div>
      <p class="cert__body">Congratulations, you have been awarded this reward.</p>
      <div class="cert__heading cert__heading--features">FEATURES</div>
      <div class="cert__lines"><div class="cert__line"></div><div class="cert__line"></div><div class="cert__line cert__line--half"></div></div>
      <div class="cert__heading cert__heading--how">HOW CAN WE DO THIS?</div>
      <div class="cert__lines cert__lines--how"><div class="cert__line"></div><div class="cert__line"></div><div class="cert__line cert__line--half"></div></div>
      <div class="cert__footer"><p class="cert__id">Certificate ID<br><b>#10983-95930</b><br>Expires 02/29/2020</p><p class="cert__site">VIEW ALL THE DETAILS OF THIS SPECIAL<br><b>WWW.PRIZEPATHREWARDS.COM</b><span class="cert__terms">Terms and conditions apply</span></p></div>
    </article>

    <article class="cert">
      <div class="cert__photo" role="img" aria-label="Cruise ship sailing on blue water" style="background:linear-gradient(180deg,#6aa8dc 0%,#a8cce8 45%,#f0f0f0 62%,#2a6aa8 100%)"></div>
      <span class="cert__compliments">Compliments Of</span>
      <span class="cert__enjoy">ENJOY</span><span class="cert__eyebrow">A 3 Night</span><span class="cert__tag">Luxury Cruise</span>
      <p class="cert__offer">A 4 Night Luxury <em>Cruise Getaway</em></p>
      <div class="cert__badge" role="img" aria-label="Beach cabana photo" style="background:linear-gradient(#5ab0e0,#d8c090)"></div>
      <div class="cert__ribbon">EXCLUSIVELY FOR : CUSTOMER NAME</div>
      <p class="cert__body">Congratulations, you have been awarded this reward.</p>
      <div class="cert__heading cert__heading--features">FEATURES</div>
      <div class="cert__lines"><div class="cert__line"></div><div class="cert__line"></div><div class="cert__line cert__line--half"></div></div>
      <div class="cert__heading cert__heading--how">HOW CAN WE DO THIS?</div>
      <div class="cert__lines cert__lines--how"><div class="cert__line"></div><div class="cert__line"></div><div class="cert__line cert__line--half"></div></div>
      <div class="cert__footer"><p class="cert__id">Certificate ID<br><b>#10983-95930</b><br>Expires 02/29/2020</p><p class="cert__site">VIEW ALL THE DETAILS OF THIS SPECIAL<br><b>WWW.PRIZEPATHREWARDS.COM</b><span class="cert__terms">Terms and conditions apply</span></p></div>
    </article>
  </section>

  <section class="cta">
    <svg class="cta__shape" width="1014" height="79" viewBox="0 0 1014 79" aria-hidden="true">
      <rect x="0" y="0" width="1014" height="79" rx="6" fill="var(--cta-blue)"/>
      <path d="M834 0 H1008 Q1014 0 1014 6 V73 Q1014 79 1008 79 H834 L868 39.5 Z" fill="var(--cta-green)"/>
    </svg>
    <p class="cta__main">GET A <strong>FREE SAMPLE PACKAGE</strong> FOR A LIMITED TIME ONLY</p>
    <p class="cta__offer">UNLIMITED<br>INCENTIVES<br>JUST <strong>$99/MTH</strong></p>
  </section>
</main>
</body>
</html>
```